Software - upgrade look and feel

Brightmile Ledgerworks is the worldwide distributor of the uPlotta software application, which powers a loan strategy as described at www.brightmileledgerworks.com.The company has recently upgraded its image and website; and now seeks to give uPlotta a much-needed face-lift.Using the screen shots of the existing application (2 x screens provided), recreate the screens in a modern and vibrant style that generates a feeling of professionalism and confidence.
Updates

Project not yet launched and I felt 5 days was inadequate.

Target Market(s)

Financial services industry and their clients.

Industry/Entity Type

Financial Service

Font styles to use
Other font styles liked:
• See our website at brightmileledgerworks.com - happy with this font, but open to ideas.

Colors

Designer to choose colors to be used in the design.

Requirements
Must have
• Existing fields, but perhaps more intuitive for the User.
Nice to have
• A less busy look that suggests an innovative software application.
Should not have
• Complication.

```html
<!DOCTYPE html>
<html lang="en">
<head>
<meta charset="utf-8">
<title>uPlotta – Step 5 Calculate</title>
<link rel="stylesheet" href="https://fonts.googleapis.com/css2?family=Arimo:wght@400;700&display=swap">
<style>
  :root{
    --teal:#4fb3a9;
    --teal-dark:#3a8a80;
    --body:#575757;
    --chart-bg:#3d3d3d;
    --tab:#d9d9d9;
    --orange:#f29d12;
    --link:#f5c46a;
    --blue:#4cc4ef;
    --coral:#f28c4c;
    --select:#3b6fc4;
    --white:#ffffff;
    --dark:#222222;
  }
  *{box-sizing:border-box;margin:0;padding:0}
  html,body{width:1200px;height:750px;overflow:hidden;background:var(--body)}
  body{font-family:"Arimo",Arial,sans-serif;color:var(--white);position:relative}
  .abs{position:absolute}
  a{color:inherit}

  .header{left:0;top:0;width:1200px;height:80px;background:var(--teal)}
  .brand{left:40px;top:22px;display:flex;align-items:center;gap:12px;font-size:32px;font-weight:400;color:var(--white)}
  .brand-mark{width:18px;height:18px;background:var(--white)}

  .tabs{left:0;top:79px;width:1200px;height:27px;display:flex;gap:2px}
  .tab{flex:1;background:var(--tab);color:var(--dark);font-size:12px;font-weight:700;display:flex;align-items:center;justify-content:center;border-radius:8px 8px 0 0;padding-top:5px}
  .tab.active{background:var(--teal-dark);color:var(--white);border:1px solid #cfe;border-bottom:0}

  .stepline{height:2px;background:#e5e5e5;top:147px}
  .stepnum{width:28px;height:28px;border-radius:50%;border:2px solid var(--white);background:var(--orange);color:var(--white);font-size:19px;display:flex;align-items:center;justify-content:center;top:134px}
  .stepnum.current{background:var(--teal)}

  .section-bar{left:20px;top:181px;width:1135px;height:26px;background:#a3a3a3;border-radius:5px;display:flex;justify-content:space-between;align-items:center;padding:0 9px 0 12px;font-weight:700;font-size:20px}

  .label{font-size:14.5px;line-height:16px}
  .link{color:var(--link);text-decoration:underline;font-size:14.5px;line-height:16px}
  .link.bold{font-weight:700}
  .field{background:var(--white);border-radius:5px;height:17px}
  .select{background:var(--white);border-radius:4px;height:17px}
  .select::after{content:"";position:absolute;right:0;top:0;width:15px;height:17px;background:var(--select);border-radius:0 4px 4px 0}
  .info{width:18px;height:18px;border-radius:50%;background:#e6e6e6;border:1px solid #9a9a9a;color:#8a8a8a;font-size:12px;font-weight:700;display:flex;align-items:center;justify-content:center;font-family:Georgia,serif}

  .chart{left:167px;top:310px;width:966px;height:201px;border:1px solid #bdbdbd}
  .ylab{width:60px;text-align:right;font-size:13.5px;line-height:14px;left:94px}
  .xlab{font-size:13.5px;top:520px;width:24px;text-align:center}
  .axis-title{font-size:14px}
  .legend-swatch{width:13px;height:13px}

  .radio{width:19px;height:19px;border-radius:50%;background:var(--white);display:flex;align-items:center;justify-content:center}
  .radio::after{content:"";width:9px;height:9px;border-radius:50%;background:#999}
  .radio.on::after{background:#111}
  .opt{font-size:14.5px}
  .button{background:var(--teal);color:var(--white);font-size:14.5px;border-radius:4px;display:flex;align-items:center;justify-content:center;height:17px;width:161px;top:706px}
</style>
</head>
<body>
  <header class="abs header"></header>
  <div class="abs brand"><span class="brand-mark"></span><span>uPlotta</span></div>

  <nav class="abs tabs">
    <div class="tab">Step 1 - Client/Income</div>
    <div class="tab">Step 2 - Expenses</div>
    <div class="tab">Step 3 - Assets/Liabilities</div>
    <div class="tab">Step 4 - Restructure</div>
    <div class="tab active">Step 5 - Calculate</div>
  </nav>

  <div class="abs stepline" style="left:142px;width:163px"></div>
  <div class="abs stepline" style="left:388px;width:163px"></div>
  <div class="abs stepline" style="left:634px;width:163px"></div>
  <div class="abs stepline" style="left:880px;width:163px"></div>
  <div class="abs stepnum" style="left:87px">1</div>
  <div class="abs stepnum" style="left:333px">2</div>
  <div class="abs stepnum" style="left:578px">3</div>
  <div class="abs stepnum" style="left:824px">4</div>
  <div class="abs stepnum current" style="left:1068px">5</div>

  <div class="abs section-bar"><span>Client Details</span><span>Daniel &amp; Rosa Finch</span></div>

  <div class="abs label" style="left:20px;top:229px">View</div>
  <a class="abs link" style="left:20px;top:252px">Loan Writer User</a>
  <a class="abs link" style="left:20px;top:274px">CS Officer</a>
  <div class="abs info" style="left:154px;top:225px">i</div>
  <div class="abs select" style="left:185px;top:224px;width:243px"></div>
  <div class="abs select" style="left:185px;top:245px;width:243px"></div>
  <div class="abs select" style="left:185px;top:268px;width:243px"></div>

  <div class="abs label" style="left:455px;top:229px">Title</div>
  <div class="abs label" style="left:455px;top:249px">Family Name</div>
  <div class="abs label" style="left:455px;top:273px">First Name</div>
  <div class="abs info" style="left:587px;top:223px">i</div>
  <div class="abs info" style="left:587px;top:246px">i</div>
  <div class="abs info" style="left:587px;top:268px">i</div>
  <div class="abs select" style="left:617px;top:223px;width:61px"></div>
  <a class="abs link" style="left:690px;top:225px">Additional Details</a>
  <div class="abs field" style="left:617px;top:245px;width:230px"></div>
  <div class="abs field" style="left:617px;top:268px;width:230px"></div>

  <div class="abs label" style="left:881px;top:229px">File No.</div>
  <div class="abs label" style="left:881px;top:249px">Email</div>
  <div class="abs info" style="left:960px;top:223px">i</div>
  <div class="abs info" style="left:960px;top:246px">i</div>
  <div class="abs field" style="left:988px;top:223px;width:184px"></div>
  <div class="abs field" style="left:988px;top:246px;width:184px"></div>
  <a class="abs link bold" style="left:883px;top:271px">Statistics</a>
  <a class="abs link bold" style="left:981px;top:271px">Send to Pending Tray</a>

  <div class="abs axis-title" style="left:42px;top:389px;transform:rotate(-90deg)">Balance</div>
  <div class="abs ylab" style="top:339px">500000</div>
  <div class="abs ylab" style="top:355px">450000</div>
  <div class="abs ylab" style="top:370px">400000</div>
  <div class="abs ylab" style="top:386px">350000</div>
  <div class="abs ylab" style="top:402px">300000</div>
  <div class="abs ylab" style="top:417px">250000</div>
  <div class="abs ylab" style="top:433px">200000</div>
  <div class="abs ylab" style="top:449px">150000</div>
  <div class="abs ylab" style="top:464px">100000</div>
  <div class="abs ylab" style="top:480px">50000</div>

  <svg class="abs chart" viewBox="0 0 877 247" preserveAspectRatio="none" role="img" aria-label="Loan balance by year, Step 3 versus Step 4">
    <rect width="877" height="247" fill="var(--chart-bg)"/>
    <g fill="var(--blue)">
      <rect x="21.5" y="48" width="19" height="199"/><rect x="49.2" y="48" width="19" height="199"/>
      <rect x="77" y="63" width="19" height="184"/><rect x="104.7" y="67" width="19" height="180"/>
      <rect x="132.4" y="72" width="19" height="175"/><rect x="160.2" y="78" width="19" height="169"/>
      <rect x="187.9" y="82" width="19" height="165"/><rect x="215.6" y="86" width="19" height="161"/>
      <rect x="243.3" y="90" width="19" height="157"/><rect x="271.1" y="94" width="19" height="153"/>
      <rect x="298.8" y="100" width="19" height="147"/><rect x="326.5" y="104" width="19" height="143"/>
      <rect x="354.3" y="110" width="19" height="137"/><rect x="382" y="114" width="19" height="133"/>
      <rect x="409.7" y="118" width="19" height="129"/><rect x="437.5" y="126" width="19" height="121"/>
      <rect x="465.2" y="132" width="19" height="115"/><rect x="492.9" y="141" width="19" height="106"/>
      <rect x="520.6" y="147" width="19" height="100"/><rect x="548.4" y="154" width="19" height="93"/>
      <rect x="576.1" y="162" width="19" height="85"/><rect x="603.8" y="168" width="19" height="79"/>
      <rect x="631.6" y="175" width="19" height="72"/><rect x="659.3" y="183" width="19" height="64"/>
      <rect x="687" y="195" width="19" height="52"/><rect x="714.8" y="202" width="19" height="45"/>
      <rect x="742.5" y="214" width="19" height="33"/><rect x="770.2" y="221" width="19" height="26"/>
      <rect x="797.9" y="230" width="19" height="17"/><rect x="825.7" y="242" width="19" height="5"/>
      <rect x="853.4" y="246" width="19" height="1"/>
    </g>
    <g fill="var(--coral)">
      <rect x="21.5" y="48" width="19" height="199"/><rect x="49.2" y="56" width="19" height="191"/>
      <rect x="77" y="74" width="19" height="173"/><rect x="104.7" y="84" width="19" height="163"/>
      <rect x="132.4" y="94" width="19" height="153"/><rect x="160.2" y="105" width="19" height="142"/>
      <rect x="187.9" y="116" width="19" height="131"/><rect x="215.6" y="126" width="19" height="121"/>
      <rect x="243.3" y="134" width="19" height="113"/><rect x="271.1" y="143" width="19" height="104"/>
      <rect x="298.8" y="154" width="19" height="93"/><rect x="326.5" y="164" width="19" height="83"/>
      <rect x="354.3" y="173" width="19" height="74"/><rect x="382" y="182" width="19" height="65"/>
      <rect x="409.7" y="193" width="19" height="54"/><rect x="437.5" y="203" width="19" height="44"/>
      <rect x="465.2" y="212" width="19" height="35"/><rect x="492.9" y="220" width="19" height="27"/>
      <rect x="520.6" y="228" width="19" height="19"/><rect x="548.4" y="236" width="19" height="11"/>
      <rect x="576.1" y="240" width="19" height="7"/><rect x="603.8" y="244" width="19" height="3"/>
    </g>
  </svg>

  <div class="abs xlab" style="left:189px">0</div><div class="abs xlab" style="left:220px">1</div>
  <div class="abs xlab" style="left:250px">2</div><div class="abs xlab" style="left:281px">3</div>
  <div class="abs xlab" style="left:311px">4</div><div class="abs xlab" style="left:342px">5</div>
  <div class="abs xlab" style="left:372px">6</div><div class="abs xlab" style="left:403px">7</div>
  <div class="abs xlab" style="left:433px">8</div><div class="abs xlab" style="left:464px">9</div>
  <div class="abs xlab" style="left:494px">10</div><div class="abs xlab" style="left:525px">11</div>
  <div class="abs xlab" style="left:555px">12</div><div class="abs xlab" style="left:586px">13</div>
  <div class="abs xlab" style="left:616px">14</div><div class="abs xlab" style="left:647px">15</div>
  <div class="abs xlab" style="left:678px">16</div><div class="abs xlab" style="left:709px">17</div>
  <div class="abs xlab" style="left:739px">18</div><div class="abs xlab" style="left:770px">19</div>
  <div class="abs xlab" style="left:800px">20</div><div class="abs xlab" style="left:831px">21</div>
  <div class="abs xlab" style="left:861px">22</div><div class="abs xlab" style="left:892px">23</div>
  <div class="abs xlab" style="left:922px">24</div><div class="abs xlab" style="left:953px">25</div>
  <div class="abs xlab" style="left:983px">26</div><div class="abs xlab" style="left:1014px">27</div>
  <div class="abs xlab" style="left:1044px">28</div><div class="abs xlab" style="left:1075px">29</div>
  <div class="abs xlab" style="left:1105px">30</div>

  <div class="abs axis-title" style="left:548px;top:536px">Terms (Yrs)</div>
  <div class="abs legend-swatch" style="left:767px;top:537px;background:var(--blue)"></div>
  <div class="abs axis-title" style="left:795px;top:536px">Step 3</div>
  <div class="abs legend-swatch" style="left:939px;top:537px;background:var(--coral)"></div>
  <div class="abs axis-title" style="left:967px;top:536px">Step 4</div>

  <div class="abs info" style="left:68px;top:588px">i</div>
  <div class="abs radio on" style="left:101px;top:588px"></div>
  <div class="abs opt" style="left:129px;top:589px">Graph - Years/Interest Saved</div>
  <div class="abs info" style="left:68px;top:672px">i</div>
  <div class="abs radio" style="left:101px;top:672px"></div>
  <div class="abs opt" style="left:128px;top:674px">Loan Comparison</div>

  <div class="abs info" style="left:426px;top:588px">i</div>
  <div class="abs radio" style="left:457px;top:588px"></div>
  <div class="abs opt" style="left:485px;top:589px">Analysis by Year</div>
  <div class="abs info" style="left:426px;top:614px">i</div>
  <div class="abs radio" style="left:457px;top:614px"></div>
  <div class="abs opt" style="left:485px;top:616px">Analysis by Month</div>
  <div class="abs info" style="left:426px;top:641px">i</div>
  <div class="abs radio" style="left:457px;top:641px"></div>
  <div class="abs opt" style="left:485px;top:643px">Analysis by Trasaction :</div>
  <div class="abs field" style="left:461px;top:672px;width:243px"></div>
  <div class="abs info" style="left:419px;top:705px">i</div>
  <a class="abs link" style="left:460px;top:705px">Report</a>

  <a class="abs link" style="left:773px;top:589px">Potential Years Saved</a>
  <a class="abs link" style="left:773px;top:616px">Potential Interest Saved</a>
  <a class="abs link" style="left:773px;top:643px">Extra Payment Savings</a>
  <a class="abs link" style="left:773px;top:672px">Offset Saving</a>
  <div class="abs info" style="left:995px;top:588px">i</div>
  <div class="abs info" style="left:995px;top:615px">i</div>
  <div class="abs field" style="left:1030px;top:589px;width:148px"></div>
  <div class="abs field" style="left:1030px;top:615px;width:148px"></div>
  <div class="abs field" style="left:1030px;top:643px;width:148px"></div>
  <div class="abs field" style="left:1030px;top:672px;width:148px"></div>

  <div class="abs button" style="left:848px">Save</div>
  <div class="abs button" style="left:1017px">Cancel</div>
</body>
</html>
```